Letter and Envelope Design For Juniper Crest Realty

Please design a letter and an envelope incorporating our logo (See Attached). We are also launched a business card contest. Since we want them to match, please feel free to submit a design for both the business card and also the letter design and envelope.

Requirements
Must have
• The envelope, the letter and the business cards must match somehow connecting the designs. We want them to have something that holds them together besides the logo.

```html
<!DOCTYPE html>
<html lang="en">
<head>
<meta charset="utf-8">
<title>Juniper Crest Realty – Stationery</title>
<link href="https://fonts.googleapis.com/css2?family=Montserrat:wght@400;500;600&family=Lato:wght@400&display=swap" rel="stylesheet">
<style>
:root{
  --navy:#26307f;
  --navy-deep:#1f2670;
  --bar-gray:#6b6b6b;
  --ink:#333;
  --muted:#555;
  --paper:#ffffff;
  --card-light:#ececec;
  --backdrop:#3a3a3a;
  --backdrop-low:#5c5c5c;
}
*{margin:0;padding:0;box-sizing:border-box}
html,body{width:1200px;height:3229px;overflow:hidden}
body{background:var(--backdrop);font-family:"Lato",sans-serif;color:var(--ink);position:relative}
.lower-backdrop{position:absolute;left:0;top:2364px;width:1200px;height:865px;background:var(--backdrop-low)}
.sheet{position:absolute;background:var(--paper);box-shadow:0 3px 8px rgba(0,0,0,.35);overflow:hidden}

/* brand lockup */
.brand{position:absolute;display:flex;align-items:center;gap:10px;color:var(--navy);font-family:"Montserrat",sans-serif;font-weight:500}
.brand-mark{border:2.5px solid var(--navy);border-radius:50%;flex:none}
.brand-name{display:flex;flex-direction:column;line-height:1.15;letter-spacing:.12em;text-transform:uppercase}
.brand-name .sub{letter-spacing:.35em;text-align:center}

/* bottom bar */
.bar{position:absolute;left:0;bottom:0;width:100%;height:6px;display:flex}
.bar .navy{background:var(--navy);width:69%}
.bar .gray{background:var(--bar-gray);flex:1}

/* letterhead */
.letter{left:251px;top:172px;width:652px;height:844px;
  background:linear-gradient(#fafafa 0,#dcdcdc 280px,#fff 282px,#f4f4f4 380px,#d9d9d9 563px,#fff 565px,#fff 700px,#d6d6d6 838px)}
.letter .brand{left:41px;top:72px}
.letter .brand-mark{width:60px;height:60px}
.letter .brand-name{font-size:17px}
.letter .brand-name .sub{font-size:12px}
.recipient{position:absolute;left:63px;top:254px;font-size:12.5px;line-height:21px}
.recipient .name{font-family:"Montserrat",sans-serif;font-weight:600;color:var(--navy);font-size:14px}
.body-copy{position:absolute;left:63px;top:356px;width:526px;font-size:12.3px;line-height:21px;text-align:justify;color:#333}
.body-copy p+p{margin-top:21px}
.signoff{position:absolute;left:63px;top:607px;font-size:11px;color:#444}
.signature{display:block;width:88px;height:28px;margin:6px 0 8px;background:linear-gradient(90deg,#cfcfcf,#e4e4e4);border-radius:4px}
.letter-footer{position:absolute;left:41px;right:45px;top:788px;display:flex;align-items:flex-end;font-family:"Montserrat",sans-serif;font-size:11px;color:#444;line-height:15px}
.letter-footer .addr{padding-right:20px;border-right:1.5px solid #666}
.letter-footer .contact{padding-left:20px}
.letter-footer .web{margin-left:auto}
.web b{color:var(--navy);font-weight:600}
.ico{display:inline-block;vertical-align:-1px;margin-right:5px}

/* envelopes */
.envelope .brand{left:30px;top:30px}
.envelope .brand-mark{width:40px;height:40px}
.envelope .brand-name{font-size:12px}
.envelope .brand-name .sub{font-size:8.5px}
.env-address{position:absolute;left:30px;border-left:1.5px solid var(--navy);padding-left:8px;font-family:"Montserrat",sans-serif;font-size:8.5px;line-height:14px;color:#444}
.env-address .co{color:var(--navy);font-weight:600}
.env-web{position:absolute;right:34px;font-family:"Montserrat",sans-serif;font-size:8.5px;color:#444}
.flap{position:absolute;left:0;top:0;width:100%}

.env-dl-front{left:82px;top:1216px;width:509px;height:226px}
.env-dl-front .env-address{top:158px}
.env-dl-front .env-web{top:185px}
.env-dl-back{left:616px;top:1216px;width:509px;height:226px}

.env-c4-back{left:132px;top:1576px;width:451px;height:637px}
.env-c4-front{left:617px;top:1576px;width:451px;height:637px}
.env-c4-front .brand{left:26px;top:34px}
.env-c4-front .env-address{left:36px;top:567px;font-size:9.5px;line-height:16px}
.env-c4-front .env-web{top:606px;right:28px;font-size:9.5px}

/* business cards */
.card{width:540px;height:310px}
.card-front{left:330px;top:2430px;background:var(--navy-deep)}
.card-front .brand{left:0;right:0;top:78px;flex-direction:column;color:#fff;gap:14px}
.card-front .brand-mark{width:84px;height:84px;border-color:#fff;border-width:3.5px}
.card-front .brand-name{font-size:27px;text-align:center}
.card-front .brand-name .sub{font-size:17px}
.card-back{left:330px;top:2800px;background:var(--card-light)}
.card-back .brand{left:230px;top:50px}
.card-back .brand-mark{width:58px;height:58px}
.card-back .brand-name{font-size:18px}
.card-back .brand-name .sub{font-size:12px}
.card-rule{position:absolute;left:30px;right:30px;top:150px;height:1.5px;background:#666}
.holder{position:absolute;left:30px;top:170px;font-family:"Montserrat",sans-serif}
.holder .name{font-size:17px;font-weight:600;color:var(--navy);letter-spacing:.02em}
.holder .role{font-size:10.5px;color:#555;margin-top:2px}
.holder ul{list-style:none;margin-top:14px;font-size:10.5px;line-height:18px;color:#444}
.card-back .env-address{left:auto;right:30px;top:176px;border:0;border-right:1.5px solid var(--navy);padding:0 8px 0 0;text-align:right;font-size:10px;line-height:16px}
</style>
</head>
<body>
<div class="lower-backdrop"></div>

<!-- Letterhead -->
<section class="sheet letter">
  <div class="brand"><span class="brand-mark"></span><span class="brand-name"><span>Juniper Crest</span><span class="sub">Realty</span></span></div>
  <div class="recipient">
    <div class="name">Dana Whitfield</div>
    <div>Manager</div>
    <div>48 Alder Lane</div>
    <div>Brookhaven, NC</div>
  </div>
  <div class="body-copy">
    <p>Lorem ipsum dolor sit amet, consectetuer adipiscing elit, sed diam nonummy nibh euismod tincidunt ut laoreet dolore magna aliquam erat volutpat. Ut wisi enim ad minim veniam, quis nostrud exerci tation ullamcorper suscipit lobortis nisl ut aliquip ex ea commodo consequat. Lorem ipsum dolor sit amet, cons ectetuer adipiscing elit, sed diam nonummy nibh euismod tincidunt ut laoreet dolore magna aliquam erat volutpat. Ut wisi enim ad minim veniam, quis nostrud exerci tation ullamcorper suscipit lobortis nisl ut aliquip ex ea commodo consequat. Lorem ipsum dolor sit amet, consectetuer adipiscing elit, sed diam nonummy nibh euismod tincidunt ut laoreet dolore magna aliquam erat volutpat. Ut wisi enim ad minim veniam,</p>
    <p>consequat. Duis autem vel eum iriure dolor in hendrerit in vulputate velit esse molestie consequat, vel illum dolore eu feugiat nulla facilisis at vero eros et accumsan .</p>
  </div>
  <div class="signoff">
    sincerely
    <span class="signature" role="img" aria-label="Handwritten signature"></span>
    Dana Whitfield
  </div>
  <footer class="letter-footer">
    <div class="addr">410 Harbor Row, Ste<br>7B Linden, VA 23519</div>
    <div class="contact">
      <div><svg class="ico" width="10" height="10" viewBox="0 0 10 10"><path d="M2 0.5l2 2-1 1.3c.6 1.3 1.7 2.4 3 3l1.3-1 2 2-1.3 1.7C4 9 1 6 .5 1.8z" fill="#26307f"/></svg>+809 555 0142</div>
      <div><svg class="ico" width="10" height="8" viewBox="0 0 10 8"><rect x=".5" y=".5" width="9" height="7" fill="none" stroke="#26307f"/><path d="M.5 .5L5 4.5 9.5 .5" fill="none" stroke="#26307f"/></svg>hello@junipercrest.com</div>
    </div>
    <div class="web">www.<b>junipercrest</b>.com</div>
  </footer>
  <div class="bar"><span class="navy"></span><span class="gray"></span></div>
</section>

<!-- DL envelope, front -->
<section class="sheet envelope env-dl-front">
  <div class="brand"><span class="brand-mark"></span><span class="brand-name"><span>Juniper Crest</span><span class="sub">Realty</span></span></div>
  <div class="env-address"><div class="co">Juniper Crest</div>410 Harbor Row, Ste<br>7B Linden, VA 23519</div>
  <div class="env-web">www.<b class="web">junipercrest</b>.com</div>
  <div class="bar"><span class="navy" style="width:72%"></span><span class="gray"></span></div>
</section>

<!-- DL envelope, back -->
<section class="sheet envelope env-dl-back">
  <svg class="flap" height="84" viewBox="0 0 509 84" preserveAspectRatio="none"><polygon points="0,0 509,0 501,84 8,84" fill="#26307f"/></svg>
</section>

<!-- C4 envelope, back -->
<section class="sheet envelope env-c4-back">
  <svg class="flap" height="73" viewBox="0 0 451 73" preserveAspectRatio="none"><polygon points="0,0 451,0 444,73 7,73" fill="#26307f"/></svg>
</section>

<!-- C4 envelope, front -->
<section class="sheet envelope env-c4-front">
  <div class="brand"><span class="brand-mark"></span><span class="brand-name"><span>Juniper Crest</span><span class="sub">Realty</span></span></div>
  <div class="env-address"><div class="co">Juniper Crest</div>410 Harbor Row, Ste<br>7B Linden, VA 23519</div>
  <div class="env-web">www.<b class="web">junipercrest</b>.com</div>
  <div class="bar"><span class="navy"></span><span class="gray"></span></div>
</section>

<!-- Business card, front -->
<section class="sheet card card-front">
  <div class="brand"><span class="brand-mark"></span><span class="brand-name"><span>Juniper Crest</span><span class="sub">Realty</span></span></div>
</section>

<!-- Business card, back -->
<section class="sheet card card-back">
  <div class="brand"><span class="brand-mark"></span><span class="brand-name"><span>Juniper Crest</span><span class="sub">Realty</span></span></div>
  <div class="card-rule"></div>
  <div class="holder">
    <div class="name">DANA WHITFIELD</div>
    <div class="role">Resident Manager</div>
    <ul>
      <li><svg class="ico" width="10" height="10" viewBox="0 0 10 10"><path d="M2 0.5l2 2-1 1.3c.6 1.3 1.7 2.4 3 3l1.3-1 2 2-1.3 1.7C4 9 1 6 .5 1.8z" fill="#26307f"/></svg>+809 555 0142</li>
      <li><svg class="ico" width="10" height="8" viewBox="0 0 10 8"><rect x=".5" y=".5" width="9" height="7" fill="none" stroke="#26307f"/><path d="M.5 .5L5 4.5 9.5 .5" fill="none" stroke="#26307f"/></svg>hello@junipercrest.com</li>
      <li><svg class="ico" width="10" height="10" viewBox="0 0 10 10"><circle cx="5" cy="5" r="5" fill="#26307f"/></svg>www.<b class="web">junipercrest</b>.com</li>
    </ul>
  </div>
  <div class="env-address"><div class="co">Juniper Crest</div>410 Harbor Row, Ste<br>7B Linden, VA 23519</div>
  <div class="bar" style="height:8px"><span class="navy" style="width:72%"></span><span class="gray"></span></div>
</section>
</body>
</html>
```